Ready mix concrete Company
Brennford Ready Mix, LLC
Project: Ready mix concrete Company
Ready mix concrete Company - Construction
Creative Brief
Professional
Ned Corvani
Owner
P.O. Box 846 Harlow Creek, OK. 74604
Ned.Corvani@mailvex.com
Colors are red, black, and white.
I have a logo...Not sure how to upload it here.

```html
<!DOCTYPE html>
<html lang="en">
<head>
<meta charset="utf-8">
<title>Brennford Ready Mix, LLC – Business Card</title>
<link href="https://fonts.googleapis.com/css2?family=Roboto:wght@400;700&display=swap" rel="stylesheet">
<style>
  :root {
    --red: #e8262c;
    --ink: #2a2a2a;
    --grey-text: #4a4a4a;
    --card: #ffffff;
    --backdrop: #ececec;
    --rule: #3a3a3a;
  }
  * { margin: 0; padding: 0; box-sizing: border-box; }
  html, body { width: 1200px; height: 914px; overflow: hidden; background: var(--backdrop); }
  body { font-family: 'Roboto', Arial, sans-serif; position: relative; }

  .business-card {
    position: absolute; left: 100px; top: 171px;
    width: 1000px; height: 572px;
    background: var(--card);
    box-shadow: 0 6px 18px rgba(0,0,0,0.12);
  }

  .brand {
    position: absolute; top: 120px; left: 0; width: 100%;
    display: flex; justify-content: center; align-items: center; gap: 14px;
  }
  .brand-square { width: 26px; height: 26px; background: var(--red); flex: none; }
  .brand-name {
    font-weight: 700; font-size: 34px; letter-spacing: 2px;
    color: var(--ink); text-transform: uppercase; white-space: nowrap;
  }

  .name-band {
    position: absolute; left: 0; top: 232px; width: 100%; height: 74px;
    border-top: 3px solid var(--rule); border-bottom: 3px solid var(--rule);
    padding: 5px 0; background: var(--card);
  }
  .name-band-fill {
    height: 100%; background: var(--red);
    display: flex; justify-content: center; align-items: center;
    color: #fff; font-size: 20px; font-weight: 400; gap: 12px;
  }

  .contact-list {
    position: absolute; left: 70px; right: 70px; top: 355px;
    display: grid; grid-template-columns: 1fr 1.7fr 1.3fr; row-gap: 22px; column-gap: 20px;
    color: var(--grey-text); font-size: 19px; font-weight: 400;
  }
  .contact-item { display: flex; align-items: center; gap: 9px; white-space: nowrap; }
  .contact-icon { width: 22px; height: 22px; flex: none; }
</style>
</head>
<body>
  <div class="business-card">
    <div class="brand">
      <span class="brand-square"></span>
      <span class="brand-name">Brennford Ready Mix, LLC</span>
    </div>

    <div class="name-band">
      <div class="name-band-fill">
        <span class="person-name">Ned Corvani</span>
        <span class="divider">|</span>
        <span class="person-title">Owner</span>
      </div>
    </div>

    <div class="contact-list">
      <div class="contact-item">
        <svg class="contact-icon" viewBox="0 0 22 22"><circle cx="11" cy="11" r="11" fill="var(--red)"/><path d="M7.5 6c1 0 1.5 2 1.8 2.6.2.5-.8 1.2-.8 1.2.6 1.5 1.7 2.6 3.2 3.2 0 0 .7-1 1.2-.8.6.3 2.6.8 2.6 1.8 0 1-1 1.6-2 1.6C9.5 15.6 6 12.1 6 8c0-1 .6-2 1.5-2z" fill="#fff"/></svg>
        <span>512-555-0146</span>
      </div>
      <div class="contact-item">
        <svg class="contact-icon" viewBox="0 0 22 22"><circle cx="11" cy="11" r="11" fill="var(--red)"/><path d="M11 4.5a4 4 0 0 1 4 4c0 3-4 8-4 8s-4-5-4-8a4 4 0 0 1 4-4z" fill="#fff"/><circle cx="11" cy="8.5" r="1.5" fill="var(--red)"/></svg>
        <span>P.O. Box 846 Harlow Creek, OK. 74604</span>
      </div>
      <div class="contact-item">
        <svg class="contact-icon" viewBox="0 0 22 22"><circle cx="11" cy="11" r="11" fill="var(--red)"/><g fill="none" stroke="#fff" stroke-width="1.3"><circle cx="11" cy="11" r="5.5"/><ellipse cx="11" cy="11" rx="2.4" ry="5.5"/><line x1="5.5" y1="11" x2="16.5" y2="11"/></g></svg>
        <span>www.brennfordmix.com</span>
      </div>
      <div class="contact-item">
        <svg class="contact-icon" viewBox="0 0 22 22"><circle cx="11" cy="11" r="11" fill="var(--red)"/><rect x="6" y="9" width="10" height="6" rx="1" fill="#fff"/><rect x="8" y="5.5" width="6" height="3.5" fill="#fff"/><rect x="8" y="12.5" width="6" height="4" fill="#fff" stroke="var(--red)" stroke-width="0.8"/></svg>
        <span>512-555-0183</span>
      </div>
      <div class="contact-item">
        <svg class="contact-icon" viewBox="0 0 22 22"><circle cx="11" cy="11" r="11" fill="var(--red)"/><rect x="7.5" y="4.5" width="7" height="13" rx="1.3" fill="#fff"/><rect x="8.7" y="6.2" width="4.6" height="8" fill="var(--red)"/><circle cx="11" cy="15.8" r="0.8" fill="var(--red)"/></svg>
        <span>512-555-0129</span>
      </div>
      <div class="contact-item">
        <svg class="contact-icon" viewBox="0 0 22 22"><circle cx="11" cy="11" r="11" fill="var(--red)"/><rect x="5.5" y="7" width="11" height="8" rx="1" fill="#fff"/><path d="M5.8 7.5 11 11.5l5.2-4" fill="none" stroke="var(--red)" stroke-width="1"/></svg>
        <span>Ned.Corvani@mailvex.com</span>
      </div>
    </div>
  </div>
</body>
</html>
```